Need Business Card for our Indian Grocery Store

Industry/Entity Type

Grocery Store

Contact Information for Business Card

Manoj Baweja
Director

Store Locations:

Maplewood
482 Elm Parade
P: 03 9172 5843

Ashgrove Park
613 Carlow Road
P: 03 9238 6014

email: kvtmarts@mailnest.example

Requirements
Must have
• Our logo Colours

```html
<!DOCTYPE html>
<html lang="en">
<head>
<meta charset="utf-8">
<title>KVT Marts – Business Card</title>
<link href="https://fonts.googleapis.com/css2?family=Montserrat:wght@400;500;600;700;800&family=Crimson+Text:ital@1&display=swap" rel="stylesheet">
<style>
  :root {
    --brand-red: #e01f26;
    --card-white: #ffffff;
    --backdrop: #2b2b2b;
    --font-text: "Montserrat", Arial, sans-serif;
    --font-script: "Crimson Text", Georgia, serif;
  }
  * { box-sizing: border-box; margin: 0; padding: 0; }
  html, body { width: 800px; height: 1200px; overflow: hidden; }
  body {
    background: var(--backdrop);
    font-family: var(--font-text);
    position: relative;
  }
  .card {
    position: absolute;
    left: 80px;
    width: 640px;
    height: 366px;
    overflow: hidden;
  }
  .card--front { top: 117px; background: var(--brand-red); }
  .card--back { top: 717px; background: var(--card-white); color: var(--brand-red); }

  .stripe {
    position: absolute;
    left: 0; right: 0;
    height: 16px;
    background: var(--card-white);
  }
  .stripe::after {
    content: "";
    position: absolute;
    left: 0; right: 0;
    top: 6px;
    height: 3px;
    background: var(--brand-red);
  }
  .stripe--top { top: 22px; }
  .stripe--bottom { bottom: 22px; }

  .brand {
    position: absolute;
    display: flex;
    flex-direction: column;
    align-items: center;
  }
  .card--front .brand { left: 0; right: 0; top: 128px; color: var(--card-white); }
  .card--back .brand { left: 40px; width: 270px; top: 148px; color: var(--brand-red); }

  .brand__name {
    font-family: var(--font-text);
    font-weight: 800;
    font-size: 52px;
    letter-spacing: 1px;
    line-height: 1;
  }
  .card--back .brand__name { font-size: 42px; }

  .brand__tagline {
    display: flex;
    align-items: center;
    gap: 10px;
    margin-top: 12px;
    font-family: var(--font-script);
    font-style: italic;
    font-size: 22px;
  }
  .card--back .brand__tagline { font-size: 18px; margin-top: 10px; }
  .brand__tagline::before,
  .brand__tagline::after {
    content: "";
    width: 26px;
    height: 1.5px;
    background: currentColor;
  }

  .name-band {
    position: absolute;
    top: 58px;
    right: 0;
    width: 330px;
    height: 34px;
    background: var(--brand-red);
    border-radius: 6px 0 0 6px;
    color: var(--card-white);
    display: flex;
    align-items: center;
    padding-left: 16px;
    gap: 8px;
  }
  .name-band__name { font-weight: 800; font-size: 16px; letter-spacing: 0.8px; text-transform: uppercase; }
  .name-band__divider { width: 1px; height: 16px; background: var(--card-white); }
  .name-band__role { font-weight: 500; font-size: 15px; letter-spacing: 0.5px; }

  .contact {
    position: absolute;
    left: 346px;
    top: 110px;
    width: 270px;
  }
  .contact__heading {
    font-weight: 700;
    font-size: 14px;
    padding-bottom: 6px;
    border-bottom: 1.5px solid var(--brand-red);
    padding-left: 8px;
  }
  .store {
    padding: 8px 0 8px 8px;
    border-bottom: 1.5px solid var(--brand-red);
    font-weight: 600;
    font-size: 14px;
    line-height: 1.3;
  }
  .contact__row { display: flex; align-items: flex-start; gap: 10px; }
  .contact__row + .contact__row { margin-top: 3px; }
  .icon { width: 14px; height: 14px; flex: none; margin-top: 2px; fill: var(--brand-red); }
  .contact__email {
    padding: 9px 0 0 8px;
    font-weight: 600;
    font-size: 14px;
  }
</style>
</head>
<body>
  <section class="card card--front" aria-label="Business card front">
    <div class="stripe stripe--top"></div>
    <div class="brand">
      <div class="brand__name">KVT Marts</div>
      <div class="brand__tagline">Fresh Choice Since 2015</div>
    </div>
    <div class="stripe stripe--bottom"></div>
  </section>

  <section class="card card--back" aria-label="Business card back">
    <div class="name-band">
      <span class="name-band__name">Manoj Baweja</span>
      <span class="name-band__divider"></span>
      <span class="name-band__role">Director</span>
    </div>

    <div class="brand">
      <div class="brand__name">KVT Marts</div>
      <div class="brand__tagline">Fresh Choice Since 2015</div>
    </div>

    <div class="contact">
      <h2 class="contact__heading">Store Locations</h2>

      <div class="store">
        <div class="contact__row">
          <svg class="icon" viewBox="0 0 24 24" aria-hidden="true"><path d="M12 2a7 7 0 0 0-7 7c0 5 7 13 7 13s7-8 7-13a7 7 0 0 0-7-7zm0 9.5A2.5 2.5 0 1 1 12 6.5a2.5 2.5 0 0 1 0 5z"/></svg>
          <div>Maplewood<br>482 Elm Parade</div>
        </div>
        <div class="contact__row">
          <svg class="icon" viewBox="0 0 24 24" aria-hidden="true"><path d="M3 9c0-3 4-5 9-5s9 2 9 5v2h-5V9H8v2H3zm3 3h12l2 8H4zm6 2a2 2 0 1 0 0 4 2 2 0 0 0 0-4z"/></svg>
          <div>03 9172 5843</div>
        </div>
      </div>

      <div class="store">
        <div class="contact__row">
          <svg class="icon" viewBox="0 0 24 24" aria-hidden="true"><path d="M12 2a7 7 0 0 0-7 7c0 5 7 13 7 13s7-8 7-13a7 7 0 0 0-7-7zm0 9.5A2.5 2.5 0 1 1 12 6.5a2.5 2.5 0 0 1 0 5z"/></svg>
          <div>Ashgrove Park<br>613 Carlow Road</div>
        </div>
        <div class="contact__row">
          <svg class="icon" viewBox="0 0 24 24" aria-hidden="true"><path d="M3 9c0-3 4-5 9-5s9 2 9 5v2h-5V9H8v2H3zm3 3h12l2 8H4zm6 2a2 2 0 1 0 0 4 2 2 0 0 0 0-4z"/></svg>
          <div>03 9238 6014</div>
        </div>
      </div>

      <div class="contact__email contact__row">
        <svg class="icon" viewBox="0 0 24 24" aria-hidden="true"><path d="M2 5h20v14H2zm2 2v.5l8 5.5 8-5.5V7zm0 3v7h16v-7l-8 5.5z"/></svg>
        <div>kvtmarts@mailnest.example</div>
      </div>
    </div>
  </section>
</body>
</html>
```